Pediatric Vision Care: Myopia Control Brochure

We are a pediatric eye care practice (ophthalmology and optometry). One of our services we offer for children is myopia control, which are strategies for slowing or stopping the progression of nearsightedness. This is a service we need to sell to parents because most insurance won't pay for it. There are different options we offer that can work well for kids in different situations: glasses with Corvane lenses, atropine eye drops, and/or special contact lenses. We need a brochure we can distribute to parents to let them know about this service that would encourage them to buy it for children who need it. Attached is our initial draft brochure created by our staff that provides text that we want to keep. The images and layout can change. We probably need at least one or two photos of kids on the brochure, because this is only something that works for children who are still growing, and the target audience is parents of 4-8 year old children.

Target Market(s)

Parents of 4-8 year old children

Font styles to use
Sans Serif

Requirements
Must have
• I'm uploading our company logo that should be included somewhere on the brochure. You can include contact information (web address, phone number) for our practice that is found on our website: http://www.brookhollowkidsvision.com/
Should not have
• This should not look childish. We need the impression to be friendly but professional, medical, expert.

```html
<!DOCTYPE html>
<html lang="en">
<head>
<meta charset="utf-8">
<title>Myopia Control Brochure</title>
<link rel="stylesheet" href="https://fonts.googleapis.com/css2?family=Poppins:wght@400;500;600;700&display=swap">
<style>
:root{
  --purple:#6b76bb;
  --orange:#f48d1d;
  --yellow:#f9c41b;
  --ink:#1f1f24;
  --black:#0b0b0d;
  --white:#ffffff;
  --mist:#e9e9ec;
  --slate:#c7ccd3;
  --page:#e4e4e6;
}
*{box-sizing:border-box;margin:0;padding:0}
html,body{width:1200px;height:1074px;overflow:hidden;background:var(--page);font-family:"Poppins",sans-serif;color:var(--ink)}
.spread{position:absolute;left:240px;width:720px;height:520px;display:flex;box-shadow:0 8px 24px rgba(0,0,0,.18);background:var(--white)}
.spread--outside{top:10px}
.spread--inside{top:544px}
.panel{position:relative;width:240px;height:520px;overflow:hidden}
.panel svg.bg{position:absolute;inset:0;width:240px;height:520px}
.photo{position:absolute}
.copy{position:absolute;font-size:7.6px;line-height:1.32;color:var(--white)}
.copy p+p{margin-top:7px}
.heading{font-weight:600;font-size:13px;line-height:1.2;margin-bottom:6px}
.heading--caps{font-weight:700;text-transform:uppercase;font-size:12px}

/* outside: myopia panel */
.myopia-copy{left:14px;top:12px;width:214px}
.diagram{left:28px;top:192px;width:150px;height:92px;border-radius:3px;background:linear-gradient(120deg,#fff 0%,#fbe3d3 40%,#e8674a 75%,#f3b08f 100%)}
.environment-copy{left:14px;top:290px;width:218px}

/* outside: contact panel */
.tagline{position:absolute;right:8px;top:226px;width:150px;text-align:center;color:rgba(235,222,208,.85);font-weight:600;line-height:1.1}
.tagline .small{font-size:11px;display:block}
.tagline .big{font-size:17px;display:block}
.team{left:18px;top:300px;width:96px;height:90px;border-radius:8px;border:2px solid var(--white);background:linear-gradient(180deg,#d8dde3 0%,#f2f3f5 55%,#aeb6c2 100%)}
.contact{position:absolute;left:0;top:400px;width:240px;text-align:center;font-size:7.4px;font-weight:500;color:var(--ink)}
.contact p{margin-bottom:9px}
.contact .address{line-height:1.3}

/* outside: cover */
.brand{position:absolute;left:0;width:240px;display:flex;align-items:center;justify-content:center;gap:6px;font-weight:500;color:var(--ink)}
.brand-dot{width:12px;height:12px;border-radius:50%;background:var(--orange)}
.brand-name{font-size:15px;line-height:1.1}
.cover .brand{top:432px}

/* inside */
.lens-circle{left:120px;top:232px;width:96px;height:96px;border-radius:50%;border:2px solid var(--white);background:radial-gradient(circle,#6fa9a9 0%,#2f6d72 70%,#1d4a4f 100%)}
.lens-copy{left:24px;top:352px;width:200px;color:var(--ink)}
.lens-copy .heading{color:var(--orange)}
.drop-circle{left:138px;top:12px;width:90px;height:90px;border-radius:50%;border:2px solid var(--white);background:radial-gradient(circle at 40% 40%,#bfd3de 0%,#2c5566 55%,#102c38 100%)}
.atropine-copy{left:44px;top:72px;width:182px}
.contacts-copy{left:14px;top:14px;width:214px}
</style>
</head>
<body>

<!-- OUTSIDE -->
<section class="spread spread--outside">
  <article class="panel panel--myopia">
    <svg class="bg" viewBox="0 0 240 520" aria-hidden="true">
      <rect width="240" height="520" fill="var(--orange)"/>
      <path d="M0,0 H225 C262,80 248,150 200,182 C170,200 120,188 0,180 Z" fill="var(--purple)"/>
      <path d="M180,212 C200,225 225,240 240,250 L240,270 C222,258 200,246 178,236 Z" fill="var(--yellow)"/>
    </svg>
    <div class="copy myopia-copy">
      <h2 class="heading">Myopia control</h2>
      <p>Myopia or nearsightedness causes blurry distance vision. Myopia is caused by the elongation of the eye, and progresses throughout childhood. Myopia is becoming increasingly common. More severe myopia and a higher glasses prescription is associated with a higher risk of eye problems involving the retina in adulthood, such as retinal problems and macular degeneration.</p>
      <p>Myopia control is meant to slow the growth of the eye, keeping the glasses prescription as low as possible and reducing the risk of ocular disease in adulthood. There are several treatment options</p>
    </div>
    <div class="photo diagram" role="img" aria-label="Diagram comparing a myopic eye and a normal eye"></div>
    <div class="copy environment-copy">
      <h2 class="heading">Environmental<br>options:</h2>
      <p>All myopic children can benefit from these lifestyle changes. It is important to get your child outdoors consistently. There is strong evidence that children who spend at least 2 hours a day outdoors are less likely to become myopic, and their myopia progresses slower than children who are outdoors less. Some studies show that increasing outdoor time by as few as 45 minutes a day is beneficial in reducing progression.</p>
      <p>There is some evidence that consistent use of screens, particularly held very close to the face, can worsen nearsightedness. We recommend limiting non academic screen time and near work, and encourage your child to use the 20-20-20 rule. Every 20 minutes take a 20 second break to look at least 20 feet away.</p>
    </div>
  </article>

  <article class="panel panel--contact">
    <svg class="bg" viewBox="0 0 240 520" aria-hidden="true">
      <rect width="240" height="520" fill="var(--slate)"/>
    </svg>
    <div class="photo" style="left:0;top:0;width:240px;height:400px;background:linear-gradient(180deg,#b9c3c4 0%,#a8b4b4 45%,#8d6a52 70%,#c2c7cc 100%)" role="img" aria-label="Clinic reception desk and waiting area"></div>
    <svg class="bg" viewBox="0 0 240 520" aria-hidden="true">
      <path d="M0,220 C60,250 120,300 240,380 L240,392 C120,320 60,280 0,250 Z" fill="var(--orange)"/>
      <path d="M0,250 C60,280 120,330 240,396 L240,404 C120,340 60,300 0,262 Z" fill="var(--yellow)"/>
    </svg>
    <div class="tagline">
      <span class="small">Every</span>
      <span class="big">Child Deserves</span>
      <span class="small">to see the world</span>
      <span class="big">clearly.</span>
    </div>
    <div class="photo team" role="img" aria-label="Clinic team in white coats"></div>
    <div class="contact">
      <p>Voice: (555) 214-0190 &nbsp; Text: (555) 214-0177</p>
      <p>Fax: (555) 214-0162</p>
      <p>appointments@brookhollowkidsvision.com</p>
      <p>www.brookhollowkidsvision.com</p>
      <p class="address">Brookhollow Kids Vision, 1820 Alder Creek Road<br>Brookhollow, VA 20000</p>
    </div>
  </article>

  <article class="panel panel--cover cover">
    <svg class="bg" viewBox="0 0 240 520" aria-hidden="true">
      <defs>
        <linearGradient id="coverFade" x1="0" y1="0" x2="0" y2="1">
          <stop offset="0" stop-color="#ffffff"/><stop offset="1" stop-color="#dcdce0"/>
        </linearGradient>
      </defs>
      <rect width="240" height="520" fill="url(#coverFade)"/>
    </svg>
    <div class="photo" style="left:0;top:0;width:240px;height:400px;clip-path:path('M0,0 H240 V210 C225,330 150,385 0,385 Z');background:linear-gradient(160deg,#f1f1f3 0%,#d9cbb8 45%,#3b4666 100%)" role="img" aria-label="Smiling boy wearing round glasses in front of an eye chart"></div>
    <svg class="bg" viewBox="0 0 240 520" aria-hidden="true">
      <path d="M240,210 C225,330 150,385 0,385 L0,380 C140,372 215,320 232,200 Z" fill="var(--purple)"/>
      <path d="M240,180 L240,215 C225,335 150,388 0,388 L0,384 C150,380 225,325 236,190 Z" fill="var(--purple)"/>
    </svg>
    <div class="brand"><span class="brand-dot"></span><span class="brand-name">Brookhollow<br>Kids Vision</span></div>
  </article>
</section>

<!-- INSIDE -->
<section class="spread spread--inside">
  <article class="panel panel--lenses">
    <svg class="bg" viewBox="0 0 240 520" aria-hidden="true">
      <rect width="240" height="520" fill="var(--white)"/>
    </svg>
    <div class="photo" style="left:0;top:0;width:240px;height:330px;clip-path:path('M0,0 H240 C268,120 232,260 140,330 H0 Z');background:linear-gradient(170deg,#ffffff 0%,#eeeeee 40%,#8fcf4f 75%,#6aa83a 100%)" role="img" aria-label="Boy in a green shirt holding glasses beside a blurred eye chart"></div>
    <svg class="bg" viewBox="0 0 240 520" aria-hidden="true">
      <path d="M240,0 C268,120 232,260 140,330 L134,330 C226,262 262,122 234,0 Z" fill="var(--orange)"/>
    </svg>
    <div class="photo lens-circle" role="img" aria-label="Close-up of a myopia control spectacle lens"></div>
    <div class="copy lens-copy">
      <h2 class="heading heading--caps">Halvorsen Corvane<br>glasses lenses</h2>
      <p>FDA market authorized Halvorsen Corvane glasses lenses have been shown to slow myopia progression by about 50% in children aged 6-12.</p>
      <p>These lenses are a great treatment option because all your child needs to do is wear glasses. They look almost identical to ordinary glasses, but use specialized optics to signal the brain to slow the growth of myopic eyes.</p>
    </div>
  </article>

  <article class="panel panel--atropine">
    <svg class="bg" viewBox="0 0 240 520" aria-hidden="true">
      <rect width="240" height="520" fill="var(--purple)"/>
    </svg>
    <div class="photo" style="left:0;top:255px;width:240px;height:265px;background:linear-gradient(180deg,#c8ccd6 0%,#9aa3b4 40%,#2c3450 75%,#d8d2c6 100%)" role="img" aria-label="Young girl in glasses drawing at a desk"></div>
    <div class="photo drop-circle" role="img" aria-label="Eyedrop falling from a dropper bottle"></div>
    <div class="copy atropine-copy">
      <h2 class="heading heading--caps">Low-dose<br>atropine</h2>
      <p>These eyedrops have been studied for over 20 years and have been shown to slow myopia progression by about 50% when used consistently.</p>
      <p>Low-dose atropine is simple to add to your daily routine. One drop is placed in each eye before bed each evening.</p>
      <p>These are ordered from a compounding pharmacy and mailed directly to your home.</p>
    </div>
  </article>

  <article class="panel panel--contacts">
    <svg class="bg" viewBox="0 0 240 520" aria-hidden="true">
      <rect width="240" height="520" fill="var(--black)"/>
    </svg>
    <div class="photo" style="left:0;top:150px;width:240px;height:160px;background:radial-gradient(circle at 65% 45%,#5aa6d8 0%,#1e4a6a 25%,#3a1a16 60%,#0b0b0d 100%)" role="img" aria-label="Soft contact lens balanced on a fingertip"></div>
    <div class="photo" style="left:0;top:300px;width:240px;height:220px;clip-path:path('M0,60 C50,10 160,-5 240,20 V220 H0 Z');background:linear-gradient(160deg,#e9e9eb 0%,#c7a17d 45%,#3f5a7a 100%)" role="img" aria-label="Curly-haired child wearing dark-framed glasses"></div>
    <svg class="bg" viewBox="0 0 240 520" aria-hidden="true">
      <path d="M0,360 C50,310 160,295 240,320 L240,312 C160,287 50,302 0,352 Z" fill="var(--orange)"/>
    </svg>
    <div class="copy contacts-copy">
      <h2 class="heading">Specialty contact lenses</h2>
      <p>FDA-approved ClearPath lenses have been shown to slow myopia progression by about 50% in children aged 8-12.</p>
      <p>Contact lenses can be a great fit for many children, especially active children or those who do not enjoy wearing glasses. Many children as young as 7 or 8 are successful at wearing contacts.</p>
    </div>
  </article>
</section>

</body>
</html>
```